IT Company Business Card design

Brisk Node is a new computer solutions business focusing on setting up servers and computer systems for small to medium sized businesses.

A business client will either request a solution, or support for a current system and we will turn up on site to provide these services.

We are bast in Christchurch, New Zealand.

We are looking for unique business card's that stand out and show off the business in a professional light.

Open to all idea's etc.

Industry/Entity Type

Computer

Requirements
Must have
• Business Logo (AI file attached)
Employee Name
Business title
Business landline number
Cell phone number
Email
Web URL
Nice to have
• Could be nice to have some keywords (possibly on the back) such as:

Business IT solutions
Network installations
Phone solutions
Server management
Software diagnostics

The above is not needed, just an idea.

```html
<!DOCTYPE html>
<html lang="en">
<head>
<meta charset="utf-8">
<title>Brisk Node – Business Card</title>
<link rel="stylesheet" href="https://fonts.googleapis.com/css2?family=Raleway:wght@300;400&display=swap">
<style>
  :root {
    --ink: #000000;
    --paper: #ffffff;
    --charcoal: #232323;
    --mid-grey: #777777;
    --light-grey: #d4d4d4;
    --brand-blue: #1f3db4;
    --brand-cyan: #2fe6f2;
  }
  * { box-sizing: border-box; margin: 0; padding: 0; }
  html, body {
    width: 1200px;
    height: 653px;
    overflow: hidden;
    background: var(--paper);
  }
  .card {
    position: relative;
    width: 1200px;
    height: 653px;
    background: var(--paper);
    font-family: "Raleway", "Helvetica Neue", Arial, sans-serif;
    color: var(--ink);
    overflow: hidden;
  }
  .block { position: absolute; }

  /* right-hand decoration */
  .side-band { left: 1097px; top: 0; width: 103px; height: 653px; background: var(--charcoal); }
  .top-bar { left: 984px; top: 22px; width: 216px; height: 32px; background: var(--light-grey); }
  .top-rule { left: 853px; top: 98px; width: 347px; height: 9px; background: var(--mid-grey); }

  /* bottom-left decoration */
  .corner-block { left: 0; top: 538px; width: 98px; height: 115px; background: var(--charcoal); }
  .corner-rule { left: 0; top: 563px; width: 355px; height: 10px; background: var(--mid-grey); }
  .corner-bar { left: 0; top: 595px; width: 218px; height: 32px; background: var(--light-grey); }

  /* main brand panel */
  .brand-panel {
    left: 49px; top: 147px; width: 1151px; height: 283px;
    background: var(--paper);
    border: 11px solid var(--ink);
    border-right: none;
  }
  .brand-mark {
    position: absolute;
    left: 466px; top: 180px;
  }
  .brand-divider {
    position: absolute;
    left: 719px; top: 183px; width: 3px; height: 214px;
    background: linear-gradient(to bottom, rgba(119,119,119,0), var(--mid-grey) 30%, var(--mid-grey) 70%, rgba(119,119,119,0));
  }
  .brand-name {
    position: absolute;
    right: 27px; top: 234px;
    font-size: 57px;
    font-weight: 300;
    letter-spacing: 3px;
    line-height: 1;
    text-transform: uppercase;
    white-space: nowrap;
  }
  .brand-url {
    position: absolute;
    right: 27px; top: 318px;
    font-size: 26px;
    font-weight: 400;
    letter-spacing: 2px;
    line-height: 1;
    text-transform: uppercase;
    white-space: nowrap;
  }

  /* contact panel */
  .contact-panel {
    left: 654px; top: 495px; width: 546px; height: 122px;
    background: var(--paper);
    border: 9px solid var(--ink);
    border-right: none;
  }
  .person-name {
    position: absolute;
    right: 27px; top: 518px;
    font-size: 36px;
    font-weight: 400;
    font-variant: small-caps;
    letter-spacing: 3px;
    line-height: 1;
    white-space: nowrap;
  }
  .name-rule {
    position: absolute;
    left: 777px; top: 560px; width: 423px; height: 1px;
    background: var(--ink);
  }
  .contact-line {
    position: absolute;
    right: 24px; top: 577px;
    font-size: 16px;
    letter-spacing: 1.5px;
    line-height: 1;
    text-transform: uppercase;
    white-space: pre;
  }
</style>
</head>
<body>
  <main class="card">
    <div class="block side-band"></div>
    <div class="block top-bar"></div>
    <div class="block top-rule"></div>

    <div class="block corner-block"></div>
    <div class="block corner-rule"></div>
    <div class="block corner-bar"></div>

    <section class="block brand-panel" aria-label="Brand"></section>
    <svg class="brand-mark" width="216" height="216" viewBox="0 0 216 216" aria-hidden="true">
      <defs>
        <linearGradient id="markFill" x1="0" y1="0" x2="1" y2="1">
          <stop offset="0" stop-color="#2fe6f2"/>
          <stop offset="1" stop-color="#1f3db4"/>
        </linearGradient>
      </defs>
      <circle cx="108" cy="108" r="104" fill="url(#markFill)"/>
    </svg>
    <div class="brand-divider"></div>
    <h1 class="brand-name">Brisk Node</h1>
    <p class="brand-url">www.brisknode.co.nz</p>

    <section class="block contact-panel" aria-label="Contact"></section>
    <h2 class="person-name">Dana Whitfield</h2>
    <div class="name-rule"></div>
    <p class="contact-line">info@brisknode.co.nz     /     P:_________</p>
  </main>
</body>
</html>
```